Maple Hollow Canine Massage Needs a Business Card Design

Maple Hollow Canine Massage is a new therapeutic canine massage company located in Nederland, Colorado. I need a business card design that include my logo and basic contact information.

Target Market(s)

Pet owners, veterinarians

Industry/Entity Type

Business

Contact Information for Business Card

Lydia Ferrow, CCMT
303.518.7269
lydia@maplehollowmassage.example
www.maplehollowmassage.example

Colors
6c459b
886aae
b8a6cd
a64599
b768aa
d3a5cc
fbed22

Requirements
Must have
• Font should be similar to font in logo.

```html
<!DOCTYPE html>
<html lang="en">
<head>
<meta charset="utf-8">
<title>Maple Hollow Canine Massage – Business Card</title>
<link rel="stylesheet" href="https://fonts.googleapis.com/css2?family=Source+Sans+3:wght@400;600&display=swap">
<style>
  :root {
    --stage: #121212;
    --card-white: #ffffff;
    --purple-deep: #6c459b;
    --purple-mid: #886aae;
    --purple-soft: #b8a6cd;
    --back-top: #b689c0;
    --back-bottom: #4b2659;
    --tab-top: #b58bc4;
    --tab-bottom: #4f2a60;
    --ink: #1d1d1d;
    --icon: #4a4a55;
    --white: #ffffff;
  }
  * { margin: 0; padding: 0; box-sizing: border-box; }
  html, body { width: 1200px; height: 900px; overflow: hidden; }
  body {
    background: var(--stage);
    font-family: "Source Sans 3", "Myriad Pro", Arial, sans-serif;
    position: relative;
  }
  .card {
    position: absolute;
    top: 170px;
    width: 347px;
    height: 561px;
    overflow: hidden;
  }
  .card-front { left: 259px; background: var(--card-white); }
  .card-back {
    left: 631px;
    background: linear-gradient(to bottom, var(--back-top) 0%, #9c6eb0 35%, #6e4182 62%, var(--back-bottom) 100%);
  }
  .tab {
    position: absolute;
    left: 101px;
    width: 144px;
    height: 30px;
    background: linear-gradient(to bottom, var(--tab-top), var(--tab-bottom));
  }
  .tab-top { top: 0; }
  .tab-bottom { bottom: 0; height: 28px; }
  .brand-mark {
    position: absolute;
    left: 0; right: 0;
    top: 62px;
    text-align: center;
  }
  .brand-dot {
    display: block;
    width: 120px;
    height: 120px;
    margin: 0 auto 18px;
    border-radius: 50%;
    background: var(--purple-soft);
  }
  .brand-name {
    font-weight: 600;
    color: var(--purple-deep);
    line-height: 1.15;
  }
  .brand-name .line-main { display: block; font-size: 24px; }
  .brand-name .line-sub { display: block; font-size: 15px; letter-spacing: 0.04em; }
  .holder {
    position: absolute;
    left: 0; right: 0;
    top: 352px;
    text-align: center;
    font-weight: 600;
    font-size: 21px;
    color: var(--purple-deep);
  }
  .holder .credential { font-size: 15px; }
  .contact {
    position: absolute;
    left: 0; right: 0;
    top: 426px;
    list-style: none;
    text-align: center;
    font-size: 15.5px;
    color: var(--ink);
    line-height: 23px;
  }
  .contact svg {
    width: 11px; height: 11px;
    vertical-align: -1px;
    margin-right: 5px;
    fill: var(--icon);
  }
  .back-name {
    position: absolute;
    left: 0; right: 0;
    top: 398px;
    text-align: center;
    color: var(--white);
    font-weight: 600;
    line-height: 1.1;
  }
  .back-name .line-main { display: block; font-size: 40px; }
  .back-name .line-sub { display: block; font-size: 20px; letter-spacing: 0.06em; margin-top: 6px; }
</style>
</head>
<body>
  <section class="card card-front" aria-label="Business card front">
    <div class="tab tab-top"></div>

    <div class="brand-mark">
      <span class="brand-dot"></span>
      <p class="brand-name">
        <span class="line-main">Maple Hollow</span>
        <span class="line-sub">Canine Massage</span>
      </p>
    </div>

    <p class="holder">Lydia Ferrow, <span class="credential">CCMT</span></p>

    <ul class="contact">
      <li>
        <svg viewBox="0 0 24 24" aria-hidden="true"><path d="M6.6 10.8a15.1 15.1 0 0 0 6.6 6.6l2.2-2.2a1 1 0 0 1 1-.25 11.4 11.4 0 0 0 3.6.57 1 1 0 0 1 1 1V20a1 1 0 0 1-1 1A17 17 0 0 1 3 4a1 1 0 0 1 1-1h3.5a1 1 0 0 1 1 1c0 1.25.2 2.45.57 3.57a1 1 0 0 1-.25 1z"/></svg>303.518.7269
      </li>
      <li>
        <svg viewBox="0 0 24 24" aria-hidden="true"><path d="M2 5h20v14H2z M2 5l10 8 10-8" fill="none" stroke="#4a4a55" stroke-width="2.4"/><path d="M2 5h20l-10 8z"/></svg>lydia@maplehollowmassage.example
      </li>
      <li>
        <svg viewBox="0 0 24 24" aria-hidden="true"><circle cx="12" cy="12" r="10"/><path d="M2 12h20M12 2c3 3 3 17 0 20M12 2c-3 3-3 17 0 20" fill="none" stroke="#ffffff" stroke-width="1.4"/></svg>www.maplehollowmassage.example
      </li>
    </ul>

    <div class="tab tab-bottom"></div>
  </section>

  <section class="card card-back" aria-label="Business card back">
    <p class="back-name">
      <span class="line-main">Maple Hollow</span>
      <span class="line-sub">Canine Massage</span>
    </p>
  </section>
</body>
</html>
```